Business card design needed

Bright Path Ahead is an online wellness program designed for people dealing with cancer to take control of their lives and bright path ahead.

Target Market(s)

initially woman aged 35 to 65 years eventaully then men

Industry/Entity Type

Business

Contact Information for Business Card

Marlena Throsby
Bright path ahead Coach
Marlena@brightpathway.com.au
M 0418392716
Skype Marlena.Throsby
local number to come
www.brightpathway.com.au

Requirements
Must have
• Business cards want to have a photo of me on the back this is a head shot. Also a small blurb " Marlena recovered and survived 2 types of cancer. She under went a transformational 12 month journey to overcome cancer naturally . Join her online coaching program to bright path ahead.

Phone number and email and skype address.
Nice to have
• Looking for something that resembles health EG abstract tree of life, or something resembling health and balance . Like lime green/apple green want modern fresh. Want only 2 colours used on the cards. Need to use the logo and Bright path ahead on website and email signature - Clean and fresh

Also would like Letter head and logo for website and email signature

```html
<!DOCTYPE html>
<html lang="en">
<head>
<meta charset="utf-8">
<title>Bright Path Ahead – Business Card</title>
<link rel="stylesheet" href="https://fonts.googleapis.com/css2?family=Alegreya:wght@500&family=Open+Sans:wght@300;400&display=swap">
<style>
  :root {
    --stage: #2a2a2a;
    --lime: #9fc63c;
    --charcoal: #4a4a4a;
    --tab-grey: #4d4d4d;
    --orange: #d9822b;
    --light-green: #a8cf45;
    --photo-light: #e9e4dc;
    --photo-mid: #c9b9a3;
    --photo-teal: #4aa7a8;
  }
  * { margin: 0; padding: 0; box-sizing: border-box; }
  html, body {
    width: 1200px; height: 1200px; overflow: hidden;
    background: var(--stage);
  }
  .stage {
    position: relative; width: 1200px; height: 1200px;
  }
  .card {
    position: absolute; left: 220px; width: 760px; height: 465px;
    overflow: hidden;
    box-shadow: 0 14px 30px rgba(0,0,0,.45);
  }
  .card--front { top: 100px; background: var(--lime); }
  .card--back  { top: 635px; background: var(--charcoal); }

  .tab {
    position: absolute; width: 28px; border-radius: 14px;
  }
  .card--front .tab { background: var(--tab-grey); }
  .card--back .tab  { background: var(--lime); }
  .tab--top-right   { right: -14px; top: 0; height: 170px; border-radius: 0 0 0 14px; }
  .tab--bottom-left { left: -14px; bottom: 0; height: 170px; border-radius: 0 14px 0 0; }

  .portrait {
    position: absolute; left: 250px; top: 0; width: 260px; height: 250px;
    border-radius: 0 0 130px 130px;
    background: radial-gradient(circle at 50% 35%, var(--photo-light) 0%, var(--photo-mid) 55%, var(--photo-teal) 100%);
  }
  .wordmark {
    font-family: "Alegreya", Georgia, serif;
    font-weight: 500;
    color: var(--orange);
    letter-spacing: .5px;
    white-space: nowrap;
  }
  .card--front .wordmark {
    position: absolute; left: 0; right: 0; top: 270px;
    text-align: center; font-size: 50px;
  }
  .card--back .wordmark {
    position: absolute; left: 200px; top: 75px; font-size: 46px;
  }
  .contact {
    position: absolute; left: 200px; top: 170px;
    font-family: "Open Sans", Arial, sans-serif;
    color: var(--light-green);
  }
  .contact__name {
    font-family: "Alegreya", Georgia, serif; font-weight: 500;
    font-size: 34px; color: var(--orange); line-height: 1.1;
  }
  .contact__title { font-size: 17px; font-weight: 400; margin-bottom: 26px; }
  .contact__line { font-size: 17px; font-weight: 300; line-height: 1.5; }
</style>
</head>
<body>
<main class="stage">
  <section class="card card--front">
    <div class="tab tab--top-right"></div>
    <div class="tab tab--bottom-left"></div>
    <div class="portrait" role="img" aria-label="Head-and-shoulders portrait photo of the coach"></div>
    <div class="wordmark">Bright Path Ahead</div>
  </section>

  <section class="card card--back">
    <div class="tab tab--top-right"></div>
    <div class="tab tab--bottom-left"></div>
    <div class="wordmark">Bright Path Ahead</div>
    <div class="contact">
      <p class="contact__name">Marlena Throsby</p>
      <p class="contact__title">Bright path ahead Coach</p>
      <p class="contact__line">0418392716</p>
      <p class="contact__line">Skype Marlena.Throsby</p>
      <p class="contact__line">Marlena@brightpathway.com.au</p>
      <p class="contact__line">www.brightpathway.com.au</p>
    </div>
  </section>
</main>
</body>
</html>
```